Environmental Plastics Infographic

We need a series of infographics that can be used individually or as a combined presentation. We'd like the combined piece to include an introduction and conclusion along with 4-5 infographics. Each infographic (information unit) should also work as a standalone. We are trying to help people visualize size proportions and ratios to put carbon footprint/life cycle data for EPS foam packaging in perspective. We are looking for something creative to help people understand what the figures represent in terms they are familiar with.
To view our typical company design/style please see our website at www.trellamark.org. Our primary RGB colors are: (187,140,9); (94,47,29); (94,138,164); and (164,167,15). Secondary RGB colors are (249,162,28) and (218,210,208). Our title/header font is DIN Next LT Pro and our copy font is Calibri 10.5 pt. We can deviate from the font specification if beneficial and welcome interesting text treatments and typography.
We want sufficient white space with easy to grasp message concept with visual components. The attachment showing data points present concepts on how to show the data impacts but are only representative of a baseline concept - we are confident a professional designer can do a much better job with better visual presentation.
Target Market(s)
The audience is international brand manufacturers (brightmoor, kavo), US legislators & government agencies.
Nice to have
- Other creative ideas on how to present this messaging is encouraged.

```html
<!DOCTYPE html>
<html lang="en">
<head>
<meta charset="utf-8">
<title>EPS Life Cycle Infographic Series</title>
<link href="https://fonts.googleapis.com/css2?family=Barlow+Condensed:wght@500;600;700;800&family=Carlito:wght@400;700&display=swap" rel="stylesheet">
<style>
  :root{
    --olive:#a4a70f;
    --olive-dark:#7f8209;
    --gold:#bb8c09;
    --brown:#5e2f1d;
    --steel:#5e8aa4;
    --steel-dark:#3e6a82;
    --orange:#f9a21c;
    --stone:#dad2d0;
    --canvas:#eeece9;
    --paper:#ffffff;
    --ink:#3a3a3a;
  }
  *{box-sizing:border-box;margin:0;padding:0}
  html,body{width:880px;height:1200px;overflow:hidden;background:var(--canvas)}
  body{font-family:"Carlito","Calibri",sans-serif;color:var(--ink)}
  .series{display:grid;grid-template-columns:1fr 1fr;grid-template-rows:repeat(3,1fr);gap:14px;padding:20px;width:880px;height:1200px}
  .panel{position:relative;background:var(--paper);overflow:hidden;box-shadow:0 1px 3px rgba(0,0,0,.15)}
  .headline{position:absolute;font-family:"Barlow Condensed",sans-serif;font-weight:800;text-transform:uppercase;line-height:.95;color:var(--olive)}
  .headline.on-band{color:#fff}
  .band{position:absolute;left:0;width:100%}
  .fact{position:absolute;background:var(--steel-dark);color:#fff;font-family:"Barlow Condensed",sans-serif;font-weight:600;text-transform:uppercase;font-size:11px;line-height:1.15;padding:7px 9px}
  .fact b{font-weight:800;color:#fff}
  .label{position:absolute;font-family:"Barlow Condensed",sans-serif;font-weight:700;text-transform:uppercase;color:var(--steel-dark);line-height:1.05}
  .label.big{font-size:20px}
  .art{position:absolute;border-radius:4px}
  .brand{position:absolute;top:14px;right:14px;display:flex;align-items:center;gap:5px;font-family:"Barlow Condensed",sans-serif;font-weight:700;font-size:13px;color:var(--gold)}
  .brand .dot{width:22px;height:22px;border-radius:50%;background:var(--gold)}
  .stat-list{position:absolute;left:22px;right:22px;list-style:none}
  .stat-list li{display:flex;align-items:center;gap:8px;background:var(--steel-dark);color:#fff;font-family:"Barlow Condensed",sans-serif;font-weight:600;text-transform:uppercase;font-size:11.5px;padding:5px 8px;margin-bottom:7px}
  .stat-list li::before{content:"";flex:none;width:9px;height:9px;border-radius:50%;background:var(--orange)}
  .accent{color:var(--gold)}
</style>
</head>
<body>
<main class="series">

  <!-- Energy use -->
  <section class="panel energy">
    <h2 class="headline" style="left:22px;top:18px;font-size:30px">EPS Life Cycle –<br>Non-Renewable<br>Energy Use</h2>
    <div class="brand"><span class="dot"></span>Trellamark</div>
    <div class="art" role="img" aria-label="Glowing incandescent lightbulb" style="left:30px;top:118px;width:100px;height:150px;background:radial-gradient(circle at 50% 35%,#fff6cf,#e9d58a 55%,#9b9b9b)"></div>
    <p class="fact" style="left:160px;top:110px;width:225px">The energy needed to make one ton of EPS equals the energy of <b>300 lightbulbs</b> burning for a full year</p>
    <p class="fact" style="left:160px;top:172px;width:225px"><b>330 hours of light for a single lightbulb</b> uses about the same</p>
    <p class="label big" style="left:30px;top:278px">One 100 watt lightbulb<br><span class="accent">= 360 MJ</span></p>
    <svg class="band" style="bottom:0" width="413" height="70" viewBox="0 0 413 70" aria-hidden="true"><path d="M0 22 Q200 -8 413 28 V70 H0Z" fill="var(--olive)"/></svg>
    <p class="headline on-band" style="left:22px;bottom:14px;font-size:20px">1 ton of EPS = <span style="color:var(--brown)">109,000 MJ</span></p>
  </section>

  <!-- Global warming -->
  <section class="panel warming">
    <h2 class="headline" style="left:22px;top:18px;font-size:30px">EPS Life Cycle –<br>Global Warming</h2>
    <p class="fact" style="left:200px;top:80px;width:190px">The global warming impact of <b>1 ton of EPS</b> equals driving an average car <b>7,700 miles</b></p>
    <div class="art" role="img" aria-label="Winding road with mile markers" style="left:215px;top:150px;width:175px;height:130px;background:linear-gradient(160deg,#4a4a4a,#2e2e2e)"></div>
    <div class="art" role="img" aria-label="Small orange car" style="left:40px;top:130px;width:150px;height:80px;background:radial-gradient(ellipse at 50% 60%,#f9a21c,#d36f10 70%,#fff)"></div>
    <svg class="band" style="bottom:0" width="413" height="110" viewBox="0 0 413 110" aria-hidden="true"><path d="M0 20 Q140 40 230 110 H0Z" fill="var(--olive)"/></svg>
    <p class="headline on-band" style="left:20px;bottom:20px;font-size:18px">1 ton of EPS<br>= 7,700 miles</p>
    <div class="art" role="img" aria-label="Stack of white EPS foam blocks" style="left:250px;top:290px;width:140px;height:70px;background:linear-gradient(180deg,#fafafa,#d8dcdf)"></div>
  </section>

  <!-- Water: pool -->
  <section class="panel water-pool">
    <div class="art" role="img" aria-label="Rectangular blue swimming pool" style="left:22px;top:22px;width:170px;height:90px;background:linear-gradient(135deg,#7fc7e8,#2f8fc0)"></div>
    <p class="label" style="left:206px;top:28px;width:185px;font-size:13px">25,000 gallons/one 40x20-foot swimming pool</p>
    <p class="fact" style="left:22px;top:130px;width:190px">The amount of water to manufacture <b>1,000 EPS</b> shipping containers fills about <b>one backyard pool</b></p>
    <p class="label" style="left:230px;top:140px;width:160px;font-size:14px">A typical EPS shipping container 15x13x12 inches weighs 2 lbs</p>
    <div class="art" role="img" aria-label="White EPS shipping container" style="left:40px;top:205px;width:140px;height:70px;background:linear-gradient(180deg,#ffffff,#d4d8db)"></div>
    <svg class="band" style="bottom:0" width="413" height="90" viewBox="0 0 413 90" aria-hidden="true"><path d="M0 30 Q210 0 413 20 V90 H0Z" fill="var(--olive)"/></svg>
    <h2 class="headline on-band" style="left:22px;bottom:14px;font-size:27px">EPS Life Cycle –<br>Water Consumption</h2>
  </section>

  <!-- Water: cooler vs box -->
  <section class="panel water-compare">
    <div class="art" role="img" aria-label="White EPS foam cooler" style="left:30px;top:22px;width:120px;height:100px;background:linear-gradient(180deg,#ffffff,#cfd4d7)"></div>
    <p class="fact" style="left:200px;top:30px;width:185px">One ton uses <b>1,200 gallons</b> of water</p>
    <p class="fact" style="left:170px;top:100px;width:215px">The amount of water used to make an EPS cooler is a <b>fraction</b> of the water a paper box requires</p>
    <div class="art" role="img" aria-label="Brown corrugated cardboard box" style="left:30px;top:150px;width:120px;height:100px;background:linear-gradient(160deg,#c99a63,#8d6236)"></div>
    <p class="label" style="left:170px;top:200px;width:210px;font-size:14px">One ton uses 3,900 gallons of water</p>
    <svg class="band" style="bottom:0" width="413" height="90" viewBox="0 0 413 90" aria-hidden="true"><path d="M0 20 Q210 0 413 30 V90 H0Z" fill="var(--olive)"/></svg>
    <h2 class="headline on-band" style="left:22px;bottom:14px;font-size:27px">EPS Life Cycle –<br>Water Consumption</h2>
  </section>

  <!-- Diverted from landfill -->
  <section class="panel diverted">
    <h2 class="headline" style="left:22px;top:20px;font-size:29px">19,850 tons EPS diverted<br><span style="color:var(--brown)">from the landfill in 2018</span></h2>
    <svg class="band" style="top:92px" width="413" height="44" viewBox="0 0 413 44" aria-hidden="true"><path d="M0 6 H413 V38 Q200 48 0 38Z" fill="var(--olive)"/></svg>
    <p class="headline on-band" style="left:22px;top:102px;font-size:20px">This EPS was used to make:</p>
    <div class="art" role="img" aria-label="Recycled products: picture frames, crown moulding and new packaging" style="left:40px;top:148px;width:330px;height:100px;background:linear-gradient(90deg,#e9e3d7,#cfc6b8)"></div>
    <div class="art" role="img" aria-label="Person taking out household waste" style="left:22px;top:268px;width:70px;height:90px;background:linear-gradient(180deg,#8fa64a,#4d5f2a)"></div>
    <p class="label" style="left:105px;top:280px;width:280px;font-size:17px">The equivalent of waste generated by<br><span class="accent" style="font-size:28px">11,222</span> U.S. households</p>
  </section>

  <!-- Recycling summary -->
  <section class="panel recycling">
    <ul class="stat-list" style="top:22px">
      <li>EPS is 98% air and fully recyclable</li>
      <li>Collected material becomes new durable goods</li>
      <li>Recycling rates keep climbing each year</li>
    </ul>
    <div class="art" role="img" aria-label="Coiled rope of densified recycled EPS" style="left:120px;top:130px;width:170px;height:130px;border-radius:50%;background:radial-gradient(circle,#fff 18%,#bfc8cd 22%,#7d8b94 60%,#e3e6e8 64%)"></div>
    <ul class="stat-list" style="top:275px">
      <li>175 million lbs recycled in the U.S.</li>
      <li>Enough to fill 4,400 trucks each year</li>
      <li>Over 1 billion lbs since 1991</li>
    </ul>
  </section>

</main>
</body>
</html>
```